New Manager Resource Guide & Planner

I need a template designed for a resource guide and planner that new managers would use to help guide them their first year managing others. Think your typical planner injected with tips, worksheets, quotes and other helpful tools. Initially, I'd like a template created for some key pages: one month, one week and single day layouts plus a quote page. I'm attaching a very rudimentary idea of the project, just need it purposefully designed with my colors and branding. The size is 6" x 8 " h. I would like this done in InDesign or Keynote so I can edit it and create other pages. Most likely, though, will contract you to finish out the entire project.

Target Market(s)

new managers (and HR directors who will most likely purchase the resource planner for their employees)

Industry/Entity Type

Advertising

Font styles to use
Other font styles liked:
• archer, open sans

Requirements
Must have
• a creative feel to it (I come from the advertising industry, so a fun design is OK). use of my branding and colors, be noticeably well designed.
Nice to have
• look at other planners for ideas. my goal is to use your template to build out the other pages I need. So think cool edging, or stylized quote boxes, etc.
Should not have
• please use the colors in my palette in the attached pdf plus any other complementary colors you see fit. my branding uses the font archer, open sans, use these and any other fonts that you see fit.

```html
<!DOCTYPE html>
<html lang="en">
<head>
<meta charset="utf-8">
<title>Month Planner</title>
<link rel="stylesheet" href="https://fonts.googleapis.com/css2?family=Raleway:wght@200&family=Open+Sans:wght@400;600&family=Zilla+Slab:wght@400;600&display=swap">
<style>
:root{
  --olive:#97a83a;
  --olive-line:#a3b043;
  --lime:#d3df5e;
  --lime-pale:#fdfef5;
  --slate:#767a80;
  --ink:#555;
  --white:#fff;
}
*{box-sizing:border-box;margin:0;padding:0}
html,body{width:1200px;height:800px;overflow:hidden;background:var(--white)}
.planner{position:relative;width:1200px;height:800px;font-family:"Open Sans",sans-serif;color:var(--ink)}
.top-band{position:absolute;left:0;top:0;width:1200px;height:6px;background:var(--olive)}
.title{position:absolute;left:29px;top:8px;font-family:"Raleway",sans-serif;font-weight:200;font-size:54px;line-height:60px;color:#b7c74a;letter-spacing:-2px;white-space:nowrap}
.rhythm-label{position:absolute;left:356px;top:14px;font-family:"Zilla Slab",serif;font-size:11px;color:#e0e6b8}
.rhythm{position:absolute;left:356px;top:28px;width:816px;height:34px}
.projects-head,.day-head{position:absolute;top:70px;height:24px;color:var(--white);font-size:15px;line-height:24px}
.projects-head{left:29px;width:320px;background:var(--slate);padding-left:13px}
.day-head{width:111px;background:var(--olive);text-align:center}
.cell{position:absolute;width:111px;height:126px;border:2px solid var(--olive-line)}
.cell::before{content:"";position:absolute;left:-2px;top:-2px;width:36px;height:22px;border:1.5px solid currentColor}
.cell.dark{color:var(--olive-line)}
.cell.pale{border-color:var(--lime);background:var(--lime-pale);color:var(--lime)}
.group-rule{position:absolute;left:42px;width:307px;height:1px;background:#999}
.task{position:absolute;left:28px;width:324px;height:16px}
.task-no{position:absolute;left:0;bottom:0;font-size:12px;color:#666;width:16px;text-align:right}
.task-line{position:absolute;left:18px;right:0;bottom:0;height:10px;border-left:1px solid #777;border-bottom:1px solid #777}
.bubbles{position:absolute;left:204px;bottom:2px;display:flex;gap:10px}
.bubbles span{display:flex;gap:1px}
.bubbles i{display:block;width:6px;height:12px;border:1px solid #666;border-radius:1px}
.hint{position:absolute;top:162px;font-size:7px;color:#c6d24a}
.foot{position:absolute;left:0;top:770px;width:1200px;height:30px;background:var(--olive);color:var(--white)}
.quote{position:absolute;left:30px;top:0;font-family:"Zilla Slab",serif;font-size:15px;line-height:30px}
.quote .mark{font-size:40px;font-weight:600;vertical-align:-12px;line-height:0}
.brand{position:absolute;right:40px;top:0;font-family:"Open Sans",sans-serif;font-weight:400;font-size:16px;line-height:30px;letter-spacing:.5px}
</style>
</head>
<body>
<div class="planner">
  <div class="top-band"></div>
  <h1 class="title">Month Planer</h1>
  <div class="rhythm-label">Work Rhythm/Puls</div>
  <svg class="rhythm" viewBox="0 0 816 34" aria-hidden="true">
    <line x1="0" y1="16" x2="816" y2="16" stroke="#d3df5e" stroke-width="1.5" stroke-dasharray="14 3"/>
    <line x1="0" y1="4" x2="816" y2="4" stroke="#bcc68a" stroke-width="1.5" stroke-dasharray="1.5 19" stroke-linecap="round"/>
    <line x1="0" y1="30" x2="816" y2="30" stroke="#bcc68a" stroke-width="1.5" stroke-dasharray="1.5 19" stroke-linecap="round"/>
  </svg>

  <div class="projects-head">PROJECTS</div>
  <div class="day-head" style="left:356px">MONDAY</div>
  <div class="day-head" style="left:473.6px">TUESDAY</div>
  <div class="day-head" style="left:591.2px">WEDNESDAY</div>
  <div class="day-head" style="left:708.8px">THURSDAY</div>
  <div class="day-head" style="left:826.4px">FRIDAY</div>
  <div class="day-head" style="left:944px">SATURDAY</div>
  <div class="day-head" style="left:1061.6px">SUNDAY</div>

  <div class="cell dark" style="left:356px;top:101px"></div><div class="cell dark" style="left:473.6px;top:101px"></div><div class="cell dark" style="left:591.2px;top:101px"></div><div class="cell dark" style="left:708.8px;top:101px"></div><div class="cell dark" style="left:826.4px;top:101px"></div><div class="cell dark" style="left:944px;top:101px"></div><div class="cell dark" style="left:1061.6px;top:101px"></div>
  <div class="cell pale" style="left:356px;top:234.6px"></div><div class="cell pale" style="left:473.6px;top:234.6px"></div><div class="cell pale" style="left:591.2px;top:234.6px"></div><div class="cell pale" style="left:708.8px;top:234.6px"></div><div class="cell pale" style="left:826.4px;top:234.6px"></div><div class="cell pale" style="left:944px;top:234.6px"></div><div class="cell pale" style="left:1061.6px;top:234.6px"></div>
  <div class="cell dark" style="left:356px;top:368.2px"></div><div class="cell dark" style="left:473.6px;top:368.2px"></div><div class="cell dark" style="left:591.2px;top:368.2px"></div><div class="cell dark" style="left:708.8px;top:368.2px"></div><div class="cell dark" style="left:826.4px;top:368.2px"></div><div class="cell dark" style="left:944px;top:368.2px"></div><div class="cell dark" style="left:1061.6px;top:368.2px"></div>
  <div class="cell pale" style="left:356px;top:501.8px"></div><div class="cell pale" style="left:473.6px;top:501.8px"></div><div class="cell pale" style="left:591.2px;top:501.8px"></div><div class="cell pale" style="left:708.8px;top:501.8px"></div><div class="cell pale" style="left:826.4px;top:501.8px"></div><div class="cell pale" style="left:944px;top:501.8px"></div><div class="cell pale" style="left:1061.6px;top:501.8px"></div>
  <div class="cell dark" style="left:356px;top:635.4px"></div><div class="cell dark" style="left:473.6px;top:635.4px"></div><div class="cell dark" style="left:591.2px;top:635.4px"></div><div class="cell dark" style="left:708.8px;top:635.4px"></div><div class="cell dark" style="left:826.4px;top:635.4px"></div><div class="cell dark" style="left:944px;top:635.4px"></div><div class="cell dark" style="left:1061.6px;top:635.4px"></div>

  <div class="group-rule" style="top:121px"></div>
  <div class="group-rule" style="top:254.6px"></div>
  <div class="group-rule" style="top:388.2px"></div>
  <div class="group-rule" style="top:521.8px"></div>
  <div class="group-rule" style="top:655.4px"></div>

  <div class="task" style="top:146px"><span class="task-no">01</span><span class="task-line"></span><span class="bubbles"><span><i></i><i></i><i></i><i></i></span><span><i></i><i></i><i></i><i></i></span></span></div>
  <div class="task" style="top:179px"><span class="task-no">02</span><span class="task-line"></span><span class="bubbles"><span><i></i><i></i><i></i><i></i></span><span><i></i><i></i><i></i><i></i></span></span></div>
  <div class="task" style="top:211px"><span class="task-no">03</span><span class="task-line"></span><span class="bubbles"><span><i></i><i></i><i></i><i></i></span><span><i></i><i></i><i></i><i></i></span></span></div>
  <div class="hint" style="left:60px">Task description. Indent for subtasks.</div>
  <div class="hint" style="left:235px">Time track bubble.</div>
  <div class="hint" style="left:311px">Total time.</div>

  <div class="task" style="top:280px"><span class="task-no">04</span><span class="task-line"></span><span class="bubbles"><span><i></i><i></i><i></i><i></i></span><span><i></i><i></i><i></i><i></i></span></span></div>
  <div class="task" style="top:312px"><span class="task-no">05</span><span class="task-line"></span><span class="bubbles"><span><i></i><i></i><i></i><i></i></span><span><i></i><i></i><i></i><i></i></span></span></div>
  <div class="task" style="top:344px"><span class="task-no">06</span><span class="task-line"></span><span class="bubbles"><span><i></i><i></i><i></i><i></i></span><span><i></i><i></i><i></i><i></i></span></span></div>

  <div class="task" style="top:413px"><span class="task-no">07</span><span class="task-line"></span><span class="bubbles"><span><i></i><i></i><i></i><i></i></span><span><i></i><i></i><i></i><i></i></span></span></div>
  <div class="task" style="top:446px"><span class="task-no">08</span><span class="task-line"></span><span class="bubbles"><span><i></i><i></i><i></i><i></i></span><span><i></i><i></i><i></i><i></i></span></span></div>
  <div class="task" style="top:478px"><span class="task-no">09</span><span class="task-line"></span><span class="bubbles"><span><i></i><i></i><i></i><i></i></span><span><i></i><i></i><i></i><i></i></span></span></div>

  <div class="task" style="top:547px"><span class="task-no">10</span><span class="task-line"></span><span class="bubbles"><span><i></i><i></i><i></i><i></i></span><span><i></i><i></i><i></i><i></i></span></span></div>
  <div class="task" style="top:579px"><span class="task-no">11</span><span class="task-line"></span><span class="bubbles"><span><i></i><i></i><i></i><i></i></span><span><i></i><i></i><i></i><i></i></span></span></div>
  <div class="task" style="top:611px"><span class="task-no">12</span><span class="task-line"></span><span class="bubbles"><span><i></i><i></i><i></i><i></i></span><span><i></i><i></i><i></i><i></i></span></span></div>

  <div class="task" style="top:680px"><span class="task-no">13</span><span class="task-line"></span><span class="bubbles"><span><i></i><i></i><i></i><i></i></span><span><i></i><i></i><i></i><i></i></span></span></div>
  <div class="task" style="top:712px"><span class="task-no">14</span><span class="task-line"></span><span class="bubbles"><span><i></i><i></i><i></i><i></i></span><span><i></i><i></i><i></i><i></i></span></span></div>
  <div class="task" style="top:744px"><span class="task-no">15</span><span class="task-line"></span><span class="bubbles"><span><i></i><i></i><i></i><i></i></span><span><i></i><i></i><i></i><i></i></span></span></div>

  <footer class="foot">
    <p class="quote"><span class="mark">“</span> Even a broken clock is right twice a day <span class="mark">”</span></p>
    <p class="brand">Northfield Studio</p>
  </footer>
</div>
</body>
</html>
```